We are a local Communty Pharmacy wishing to promote and market a specialised Pharmaceutical Service

We would like a design that is professional and enticing ( according to the brief In attached files)
We wish to Market Compounding Pharmacy as a specialist side of our business.
We have the expertise a purpose built preparation laboratory.
The main purpose is an Internet presence that entices prospective patients to contact or visit our physical store.

Target Market(s)

Patients Medicos and Veterinary clients

Industry/Entity Type

Pharmacy

Coding

Coded - Design and coding required

Number of Pages Required

1 page

Requirements
Must have
• Clear friendly image
Nice to have
• soft enticing feel
Should not have
• No crass loud unprofessional elements

```html
<!DOCTYPE html>
<html lang="en">
<head>
<meta charset="utf-8">
<title>Brightvale Compounding Pharmacy</title>
<link href="https://fonts.googleapis.com/css2?family=Open+Sans:wght@400;600;700;800&family=Oswald:wght@400;500&display=swap" rel="stylesheet">
<style>
:root{
  --navy:#0f3e7a;
  --blue:#1f8fd6;
  --sky:#47b3ea;
  --green:#1fa84a;
  --green-dark:#178a3b;
  --orange:#f5a21b;
  --text:#555b63;
  --light:#eef3f7;
  --white:#ffffff;
}
*{margin:0;padding:0;box-sizing:border-box}
html,body{width:1200px;height:2236px;overflow:hidden}
body{font-family:"Open Sans",Arial,sans-serif;background:var(--white);color:var(--text);position:relative}

.site-header{position:absolute;left:0;top:0;width:1200px;height:90px;background:var(--white)}
.brand{position:absolute;left:88px;top:24px;display:flex;align-items:center;gap:10px}
.brand-mark{width:40px;height:40px;background:var(--green);border-radius:50%}
.brand-name{font-weight:700;font-size:17px;color:var(--navy);line-height:1.1;width:150px}
.main-nav{position:absolute;left:560px;top:0;width:640px;height:28px;background:var(--navy);display:flex;justify-content:space-around;align-items:center}
.main-nav a{color:var(--white);font-size:10px;font-weight:600;text-decoration:none;letter-spacing:.5px}
.header-info{position:absolute;top:40px;display:flex;gap:8px;font-size:10px;line-height:1.5;color:var(--text)}
.header-info svg{flex:none;margin-top:2px}
.header-info.address{left:530px}
.header-info.contact{left:840px;flex-direction:column;gap:2px}
.contact-line{display:flex;gap:6px;align-items:center;white-space:nowrap}

.hero{position:absolute;left:0;top:90px;width:1200px;height:670px;background:linear-gradient(100deg,#dfe9f1 0%,#f4f7fa 40%,#e6eef4 62%,#c9d9e6 100%)}
.hero-caption{position:absolute;left:88px;top:558px}
.hero-title{background:var(--navy);color:var(--white);font-family:"Oswald",Arial,sans-serif;font-size:30px;padding:6px 26px;width:440px;letter-spacing:.5px}
.hero-sub{background:var(--blue);color:var(--white);font-size:16px;padding:8px 26px;width:440px;letter-spacing:.5px}

.about{position:absolute;left:88px;top:790px;width:1024px}
.about h2{font-family:"Oswald",Arial,sans-serif;font-weight:500;font-size:32px;color:var(--blue);margin-bottom:34px}
.about h2 span{color:var(--navy)}
.about p{font-size:11px;line-height:1.8;margin-bottom:30px}

.features{position:absolute;left:0;top:1400px;width:1200px;text-align:center}
.features h3{font-family:"Oswald",Arial,sans-serif;font-weight:400;font-size:32px;line-height:48px;color:var(--navy);margin-bottom:132px}
.feature-grid{display:flex;justify-content:center;gap:50px}
.feature-card{width:240px;height:340px;color:var(--white);padding-top:48px;display:flex;flex-direction:column;align-items:center}
.feature-card.vet{background:var(--green)}
.feature-card.scar{background:var(--sky)}
.feature-card.thyroid{background:var(--orange)}
.feature-icon{width:96px;height:96px;border:3px solid var(--white);border-radius:50%;background:rgba(255,255,255,.15);margin-bottom:40px}
.feature-card h4{font-size:18px;font-weight:600;margin-bottom:10px}
.feature-card p{font-size:11px;line-height:1.5;width:170px}

.site-footer{position:absolute;left:0;top:1960px;width:1200px;height:276px;background:var(--green)}
.footer-block{position:absolute;top:36px;color:var(--white)}
.footer-block h5{font-family:"Oswald",Arial,sans-serif;font-weight:400;font-size:28px;margin-bottom:18px}
.hours{left:210px;width:220px}
.hours-row{display:flex;gap:12px;align-items:center;font-size:11px;line-height:1.6;white-space:nowrap}
.hours-time{font-size:15px;font-weight:600}
.map{position:absolute;left:450px;top:32px;width:330px;height:190px;background:linear-gradient(135deg,#e8eef0,#cfdad6)}
.contact-block{left:820px}
.contact-block .contact-line{font-size:11px;margin-bottom:8px}
.copyright{position:absolute;left:820px;top:232px;font-size:9px;color:var(--white)}
</style>
</head>
<body>

<header class="site-header">
  <div class="brand">
    <span class="brand-mark"></span>
    <span class="brand-name">Brightvale Compounding Pharmacy</span>
  </div>
  <nav class="main-nav">
    <a href="#">HOME</a><a href="#">ABOUT US</a><a href="#">LOCATIONS</a><a href="#">TIMINGS</a><a href="#">CONTACT US</a>
  </nav>
  <div class="header-info address">
    <svg width="12" height="16" viewBox="0 0 12 16"><path d="M6 0C2.7 0 0 2.6 0 5.8 0 10 6 16 6 16s6-6 6-10.2C12 2.6 9.3 0 6 0zm0 8.2A2.4 2.4 0 1 1 6 3.4a2.4 2.4 0 0 1 0 4.8z" fill="#f5a21b"/></svg>
    <div>BRIGHTVALE COMPOUNDING PHARMACY<br>SHOP 4, 12 WILLOW ROAD, BRIGHTVALE<br>WESTERN REGION</div>
  </div>
  <div class="header-info contact">
    <div class="contact-line"><svg width="12" height="12" viewBox="0 0 12 12"><path d="M2.5 0l2 3-1.3 1.3a7 7 0 0 0 4.5 4.5L9 7.5l3 2-1.5 2.5C5 12 0 7 0 1.5z" fill="#f5a21b"/></svg>08 5550 1420</div>
    <div class="contact-line"><svg width="12" height="12" viewBox="0 0 12 12"><path d="M2.5 0l2 3-1.3 1.3a7 7 0 0 0 4.5 4.5L9 7.5l3 2-1.5 2.5C5 12 0 7 0 1.5z" fill="#f5a21b"/></svg>08 5550 1421</div>
    <div class="contact-line"><svg width="12" height="10" viewBox="0 0 12 10"><rect width="12" height="10" fill="#f5a21b"/><path d="M0 0l6 5 6-5" stroke="#fff" fill="none"/></svg>hello@brightvalecompounding.example</div>
  </div>
</header>

<section class="hero" role="img" aria-label="Smiling pharmacist in a white coat standing in front of pharmacy shelves">
  <div class="hero-caption">
    <div class="hero-title">COMPOUNDIND PHARMACY</div>
    <div class="hero-sub">IS CUSTOMISED MEDICATIONS FOR PATIENTS</div>
  </div>
</section>

<section class="about">
  <h2>WHAT IS <span>COMPOUNDING PHARMACY?</span></h2>
  <p>Well crafted remedies start here. The practice of preparing medicines has been passed down from earlier centuries and remains a valued skill within modern community pharmacy.</p>
  <p>Pharmacists once mixed nearly every prescription by hand. Today the craft returns to meet needs that factory made medicines cannot always serve for every patient.</p>
  <p>We are one of a small group of pharmacies with a dedicated preparation laboratory, allowing us to tailor strength, form and flavour to suit each person and their routine.</p>
  <p>Compounding pharmacy blends traditional skill with current technology to create unique medicines prescribed by your doctor, specialist or veterinarian.</p>
  <p>A pharmacist can adjust doses, remove allergens, or change a tablet into a liquid, cream or lozenge when a patient needs a different approach.</p>
  <p>Our team has completed further training and keeps up with new research so that every preparation meets strict quality and safety standards.</p>
  <p>We source our raw materials from trusted suppliers and follow careful procedures in a clean, purpose built space.</p>
  <p>Brightvale Compounding Pharmacy is accredited under national quality programs, giving prescribers and patients confidence in every product we prepare.</p>
  <p>Our goal is to work closely with you and your prescriber to find the right medicine in the right form for better outcomes.</p>
</section>

<section class="features">
  <h3>FEATURE ITEMS</h3>
  <div class="feature-grid">
    <div class="feature-card vet">
      <div class="feature-icon" role="img" aria-label="Animal icon for veterinary care"></div>
      <h4>VET ARTICLE</h4>
      <p>Tailored doses and flavours for pets and farm animals.</p>
    </div>
    <div class="feature-card scar">
      <div class="feature-icon" role="img" aria-label="Skin care icon for scar therapy"></div>
      <h4>SCAR THERAPY</h4>
      <p>Custom creams prepared to help skin heal and soften.</p>
    </div>
    <div class="feature-card thyroid">
      <div class="feature-icon" role="img" aria-label="Thyroid icon"></div>
      <h4>THYROID EXTRACT</h4>
      <p>Precise thyroid doses made to your prescriber's order.</p>
    </div>
  </div>
</section>

<footer class="site-footer">
  <div class="footer-block hours">
    <h5>HOURS</h5>
    <div class="hours-row">
      <svg width="40" height="40" viewBox="0 0 44 44"><circle cx="22" cy="22" r="19" fill="none" stroke="#fff" stroke-width="3"/><path d="M22 10v12l8 6" stroke="#fff" stroke-width="3" fill="none"/></svg>
      <div>7 DAYS A WEEK<br><span class="hours-time">8.30 AM TO 8.30 PM</span></div>
    </div>
  </div>
  <div class="map" role="img" aria-label="Street map showing the Brightvale pharmacy location"></div>
  <div class="footer-block contact-block">
    <h5>CONTACT US</h5>
    <div class="contact-line"><svg width="12" height="12" viewBox="0 0 12 12"><path d="M2.5 0l2 3-1.3 1.3a7 7 0 0 0 4.5 4.5L9 7.5l3 2-1.5 2.5C5 12 0 7 0 1.5z" fill="#fff"/></svg>08 5550 1420</div>
    <div class="contact-line"><svg width="12" height="12" viewBox="0 0 12 12"><path d="M2.5 0l2 3-1.3 1.3a7 7 0 0 0 4.5 4.5L9 7.5l3 2-1.5 2.5C5 12 0 7 0 1.5z" fill="#fff"/></svg>08 5550 1421</div>
    <div class="contact-line"><svg width="12" height="10" viewBox="0 0 12 10"><rect width="12" height="10" fill="#fff"/><path d="M0 0l6 5 6-5" stroke="#1fa84a" fill="none"/></svg>hello@brightvalecompounding.example</div>
  </div>
  <div class="copyright">Brightvale © 2015 All Rights Reserved</div>
</footer>

</body>
</html>
```